Ferncrest Dental, LLC business card project

Business card to be designed with current logo.
Dental office- please keep design of card that looks clean and professional.
Please include the following info:
Ferncrest Dental, LLC
Dr. Lorna Pettigrew
2871 Marlowe Street
Bethlehem, PA 18093
610-555-0193
ferncrestdental.office@examplemail.test
Hello everyone-
Reason: Just got back from overseas- will look at all designs and provide feedback. Thank you!
Reason: Polling my friends for the final selection-
thank you to all those that participated- so many talented designers!

```html
<!DOCTYPE html>
<html lang="en">
<head>
<meta charset="utf-8">
<title>Ferncrest Dental, LLC — Business Card</title>
<link rel="stylesheet" href="https://fonts.googleapis.com/css2?family=Alfa+Slab+One&family=Arimo:wght@400&display=swap">
<style>
  :root {
    --paper: #f4f4f4;
    --paper-edge: #e6e6e6;
    --green-deep: #1f9a3a;
    --green-mid: #34ad48;
    --green-light: #8cc63f;
    --green-crest: #b9e08a;
    --ink: #111111;
    --ink-soft: #1a1a1a;
    --grey-faint: #dcdcdc;
    --logo-green: #7cbf3a;
  }
  * { margin: 0; padding: 0; box-sizing: border-box; }
  html, body {
    width: 1200px; height: 685px; overflow: hidden;
    background: var(--paper);
  }
  .card {
    position: relative;
    width: 1200px; height: 685px;
    background: radial-gradient(ellipse at 45% 35%, #fbfbfb 0%, var(--paper) 55%, var(--paper-edge) 100%);
    overflow: hidden;
    font-family: "Arimo", Arial, sans-serif;
  }
  .wave { position: absolute; inset: 0; width: 1200px; height: 685px; }
  .brand-mark {
    position: absolute; top: 24px; right: 46px;
    display: flex; align-items: center; gap: 10px;
    font-family: "Arimo", Arial, sans-serif;
    font-size: 38px; color: var(--logo-green);
  }
  .brand-mark .dot {
    width: 14px; height: 14px; border-radius: 50%;
    background: var(--logo-green);
  }
  .doctor-name {
    position: absolute; left: 345px; top: 238px;
    font-family: "Alfa Slab One", Georgia, serif;
    font-size: 50px; color: var(--ink); letter-spacing: 0.5px;
  }
  .practice-name {
    position: absolute; left: 306px; top: 300px;
    font-family: "Alfa Slab One", Georgia, serif;
    font-size: 50px; letter-spacing: 0.5px;
  }
  .practice-name .first { color: var(--green-deep); }
  .practice-name .second { color: var(--green-light); }
  .practice-name .suffix { color: var(--grey-faint); }
  .address {
    position: absolute; left: 87px; top: 488px;
    font-size: 32px; line-height: 36px; color: var(--ink-soft);
  }
  .phone {
    position: absolute; left: 902px; top: 502px;
    display: flex; align-items: center; gap: 14px;
    font-size: 32px; color: var(--ink-soft);
  }
  .phone svg { width: 36px; height: 36px; }
  .email {
    position: absolute; left: 0; right: 0; top: 610px;
    text-align: center; padding-left: 50px;
    font-size: 32px; color: var(--ink-soft);
  }
</style>
</head>
<body>
  <main class="card">
    <svg class="wave" viewBox="0 0 1200 685" role="img" aria-label="Green wave band with soft swirl pattern">
      <defs>
        <linearGradient id="band-fill" x1="0" y1="0" x2="1" y2="1">
          <stop offset="0" stop-color="var(--green-mid)"/>
          <stop offset="1" stop-color="var(--green-deep)"/>
        </linearGradient>
      </defs>
      <path d="M0 432 C 180 400 330 420 560 470 C 780 515 960 410 1200 368 L1200 685 L0 685 Z" fill="var(--green-crest)"/>
      <path d="M0 446 C 180 414 330 434 560 484 C 780 529 960 424 1200 382 L1200 685 L0 685 Z" fill="url(#band-fill)"/>
    </svg>

    <div class="brand-mark"><span class="dot"></span><span>Ferncrest Dental</span></div>

    <h1 class="doctor-name">Dr. Lorna Pettigrew</h1>
    <p class="practice-name"><span class="first">Ferncrest</span> <span class="second">Dental</span><span class="suffix">, LLC</span></p>

    <address class="address" style="font-style:normal">2871 Marlowe Street<br>Bethlehem, PA 18093</address>

    <p class="phone">
      <svg viewBox="0 0 36 36" aria-hidden="true">
        <circle cx="18" cy="18" r="16" fill="none" stroke="var(--ink)" stroke-width="3"/>
        <path d="M13 10 l4 4 -2.5 2.5 c1.2 2.5 3 4.3 5.5 5.5 l2.5 -2.5 4 4 -3 3 c-6 -1 -12.5 -7.5 -13.5 -13.5 z" fill="var(--ink)"/>
      </svg>
      <span>610-555-0193</span>
    </p>

    <p class="email">ferncrestdental.office@examplemail.test</p>
  </main>
</body>
</html>
```